New All Natural Skin Care company needs logo and label design for a new skin serum product

We need a name, logo, and label design for a new company that is producing an all in one all natural highly effective skin serum. The end result should include image imposed on clear 120z plastic bottle

We would like to see designs that promote an authentic, all natural, highly effective brand image. We need the product to standout amongst the crowded store shelves. The target customer includes Greenmarrow, Pell Cortway, and other upscale supermarket and drug store chains. This is an all in one skin product that aims to simplify a very crowded field and over cluttered market segment.

Reason: Need some great designs. Something very unique that stands out on the crowded store shelves.

Target Market(s)

men and woman, 25 years and older, who are healthy and care about their skin appearance

Industry/Entity Type

Plastic

Requirements
Nice to have
• I was inspired by a juice company called Fernjarpress.example Please check it out for inspiration.

I am also inspired by mistolvane.example but am looking for more modern approach

I am interested in seeing the ingredients and benefits listed somewhere on the bottle. Here are some of them:

Jojoba Oil-moisturizing and soothing
Vitamin A-Anti Aging, Reduces wrinkles
Vitamin B-Anti Inflammatory
Vitamin C-Promote Collagen
Vitamin D3-Helps skin conditions
Vitamin E-Antioxidant
Squalene-Natural Moisturizing
Calsium Gluconate-Anti-Microbial
Acai-
Aloe-
Japanese Green Tea-anti-inflammatory
Glycerin-Moisturizing

```html
<!DOCTYPE html>
<html lang="en">
<head>
<meta charset="utf-8">
<title>Velorin Effective Skin Serum Label</title>
<link rel="stylesheet" href="https://fonts.googleapis.com/css2?family=Inter:wght@300;400;600;700&display=swap">
<style>
  :root {
    --label-blue: #00b2d6;
    --badge-teal: #0b4a57;
    --paper: #ffffff;
    --ink-light: #ffffff;
    --art-light: #ffffff;
    --art-soft: #d9f4fa;
  }
  html, body {
    margin: 0;
    padding: 0;
    overflow: hidden;
  }
  .canvas {
    position: relative;
    width: 1200px;
    height: 1000px;
    background: var(--paper);
    overflow: hidden;
    font-family: "Inter", Arial, sans-serif;
  }
  .label {
    position: absolute;
    left: 159px;
    top: 66px;
    width: 312px;
    height: 790px;
    background: var(--label-blue);
    border-radius: 10px;
    color: var(--ink-light);
  }
  .label-rules {
    position: absolute;
    left: 0;
    top: 0;
  }
  .hero-art {
    position: absolute;
    left: 84px;
    top: 0;
    width: 144px;
    height: 224px;
    border-radius: 72px 72px 72px 72px / 90px 90px 72px 72px;
    background: linear-gradient(180deg, var(--art-soft) 0%, var(--art-light) 60%);
  }
  .size-mark {
    position: absolute;
    left: 13px;
    top: 21px;
    font-size: 12px;
    font-weight: 400;
  }
  .tagline {
    position: absolute;
    left: 0;
    width: 100%;
    top: 259px;
    text-align: center;
    font-size: 18px;
    font-weight: 300;
    letter-spacing: 0.3px;
  }
  .product-name {
    position: absolute;
    left: 0;
    width: 100%;
    text-align: center;
    font-weight: 700;
    font-size: 70px;
    line-height: 1;
    margin: 0;
  }
  .product-name.skin { top: 278px; letter-spacing: 8px; text-indent: 8px; }
  .product-name.serum { top: 378px; letter-spacing: 5px; text-indent: 5px; }
  .ingredients {
    position: absolute;
    left: 0;
    width: 100%;
    top: 508px;
    margin: 0;
    padding: 0;
    list-style: none;
    text-align: center;
    font-size: 13.4px;
    line-height: 16.5px;
    font-weight: 400;
  }
  .website {
    position: absolute;
    left: 0;
    width: 100%;
    top: 749px;
    text-align: center;
    font-size: 15px;
    font-weight: 700;
  }
  .new-badge {
    position: absolute;
    left: 419px;
    top: 22px;
    width: 96px;
    height: 96px;
    border-radius: 50%;
    background: var(--badge-teal);
    color: var(--ink-light);
    display: flex;
    align-items: center;
    justify-content: center;
    font-size: 25px;
    font-weight: 700;
  }
  .brand {
    position: absolute;
    left: 215px;
    width: 200px;
    top: 906px;
    display: flex;
    flex-direction: column;
    align-items: center;
    gap: 10px;
    color: var(--label-blue);
  }
  .brand-square {
    width: 28px;
    height: 34px;
    background: var(--label-blue);
  }
  .brand-name {
    font-size: 20px;
    font-weight: 700;
    letter-spacing: 2px;
  }
</style>
</head>
<body>
<main class="canvas">
  <section class="label">
    <div class="hero-art" role="img" aria-label="White water drop illustration"></div>
    <svg class="label-rules" width="312" height="790" viewBox="0 0 312 790" aria-hidden="true">
      <line x1="70" y1="270" x2="111" y2="270" stroke="#ffffff" stroke-width="1.5"/>
      <line x1="202" y1="270" x2="242" y2="270" stroke="#ffffff" stroke-width="1.5"/>
      <line x1="28" y1="369" x2="284" y2="369" stroke="#ffffff" stroke-width="1.5"/>
      <line x1="28" y1="468" x2="284" y2="468" stroke="#ffffff" stroke-width="1.5"/>
    </svg>
    <div class="size-mark">120z</div>
    <div class="tagline">effective</div>
    <h1 class="product-name skin">SKIN</h1>
    <h2 class="product-name serum">SERUM</h2>
    <ul class="ingredients">
      <li>Jojoba Oil-moisturizing and soothing</li>
      <li>Vitamin A-Anti Aging, Reduces wrinkles</li>
      <li>Vitamin B-Anti Inflammatory</li>
      <li>Vitamin C-Promote Collagen</li>
      <li>Vitamin D3-Helps skin conditions</li>
      <li>Vitamin E-Antioxidant</li>
      <li>Squalene-Natural Moisturizing</li>
      <li>Calsium Gluconate-Anti-Microbial</li>
      <li>Acai-</li>
      <li>Aloe-</li>
      <li>Japanese Green Tea-anti-inflammatory</li>
      <li>Glycerin-Moisturizing</li>
    </ul>
    <div class="website">www.velorin.example</div>
  </section>
  <div class="new-badge">New</div>
  <div class="brand">
    <span class="brand-square" aria-hidden="true"></span>
    <span class="brand-name">VELORIN</span>
  </div>
</main>
</body>
</html>
```